Website design: professional but personally
Needs:
Our visitors are mostly people that look for a IT or technical jobs, but our customers are also visiting our website.
Core values are: personally, professional, ambition, growth, personal development
Terms that we think of are:
Professional, but personal (we ware no trading company, but we do have internation customers)
People
IT (jobs)
Engineering (jobs)

```html
<!DOCTYPE html>
<html lang="nl">
<head>
<meta charset="utf-8">
<title>Werkwijs – Vacatures in IT en techniek</title>
<link href="https://fonts.googleapis.com/css2?family=Poppins:wght@400;500;600;700&family=Open+Sans:wght@400;600&display=swap" rel="stylesheet">
<style>
:root{
  --green:#8dc63f;
  --green-dark:#7ab32e;
  --red:#e2392d;
  --red-dark:#c92c22;
  --grey-bg:#ececec;
  --text:#8a8a8a;
  --heading:#4a4a4a;
  --dark:#2d2d2d;
  --footer:#2b2b2b;
  --white:#ffffff;
  --line:#e2e2e2;
}
*{box-sizing:border-box;margin:0;padding:0}
html,body{width:1200px;height:2620px;overflow:hidden}
body{position:relative;background:var(--white);font-family:"Open Sans",Arial,sans-serif;color:var(--text)}
.abs{position:absolute}
.heading{font-family:"Poppins",Arial,sans-serif;font-weight:600;text-transform:uppercase;letter-spacing:.5px}
.section-title{position:absolute;left:0;width:1200px;text-align:center;color:var(--green);font-size:15px}

/* nav */
.nav{position:absolute;top:0;left:0;width:1200px;height:66px;background:var(--white)}
.nav a{position:absolute;top:23px;font-family:"Poppins",sans-serif;font-weight:600;font-size:12px;color:var(--heading);text-decoration:none;letter-spacing:.4px}
.nav .active{background:var(--green);color:var(--white);padding:2px 6px;top:21px}
.brand{position:absolute;left:522px;top:14px;width:156px;height:36px;display:flex;align-items:center;justify-content:center;gap:8px;font-family:"Poppins",sans-serif;font-weight:700;font-size:22px;color:var(--dark);letter-spacing:1px}
.brand i{display:block;width:10px;height:10px;background:var(--green)}
.menu-icon{position:absolute;left:888px;top:26px;width:12px}
.menu-icon span{display:block;height:2px;background:var(--heading);margin-bottom:3px}

/* hero */
.hero{position:absolute;top:66px;left:0;width:1200px;height:312px;background:linear-gradient(100deg,#6d4a3a 0%,#b98b63 22%,#e7c9a6 40%,#d8b08c 55%,#8a5c4a 72%,#c8504c 88%,#a63a3c 100%)}
.hero-shade{position:absolute;inset:0;background:rgba(40,25,20,.25)}
.hero-title{position:absolute;top:132px;left:0;width:1200px;text-align:center;color:var(--white);font-size:16px}
.search{position:absolute;top:244px;left:290px;height:40px;display:flex}
.search-field{width:288px;background:var(--red);color:var(--white);display:flex;align-items:center;padding-left:14px;gap:14px;font-family:"Poppins",sans-serif;font-weight:600;font-size:10.5px}
.search-select{width:164px;background:var(--red);border-left:1px solid var(--red-dark);color:var(--white);display:flex;align-items:center;justify-content:space-between;padding:0 14px;font-family:"Poppins",sans-serif;font-weight:600;font-size:10.5px}
.search-btn{margin-left:6px;width:160px;background:var(--green);color:var(--white);display:flex;align-items:center;justify-content:center;font-family:"Poppins",sans-serif;font-weight:600;font-size:13px}

/* featured vacancies */
.featured{position:absolute;top:378px;left:0;width:1200px;height:348px;background:var(--grey-bg)}
.job-card{position:absolute;top:452px;width:184px;height:198px;background:var(--white);padding:14px 12px 0}
.job-title{font-family:"Poppins",sans-serif;font-weight:600;font-size:11px;color:var(--heading);text-transform:uppercase;line-height:14px}
.job-title.highlight{color:var(--white)}
.job-title.highlight span{background:var(--green)}
.job-badge{position:absolute;top:14px;right:8px;background:var(--red);color:var(--white);font-family:"Poppins",sans-serif;font-size:5.5px;font-weight:600;padding:1px 3px;text-transform:uppercase}
.job-meta{margin-top:4px;display:flex;align-items:center;gap:8px;font-family:"Poppins",sans-serif;font-size:7px;text-transform:uppercase;color:#b0b0b0}
.job-meta::before{content:"";flex:1;height:1px;background:var(--line)}
.job-text{margin-top:10px;font-size:10px;line-height:15.5px;height:124px;overflow:hidden}
.read-more{position:absolute;left:42px;bottom:-12px;display:flex;height:22px}
.read-more b{width:88px;background:var(--green);color:var(--white);font-family:"Poppins",sans-serif;font-size:10px;font-weight:600;display:flex;align-items:center;justify-content:center}
.arrow-box{width:18px;height:18px;margin:2px 0 0 -4px;background:var(--red);transform:rotate(45deg);display:flex;align-items:center;justify-content:center}
.arrow-box svg{transform:rotate(-45deg)}
.all-jobs{position:absolute;top:706px;left:538px;width:120px;height:36px;background:var(--red);color:var(--white);font-size:10.5px;display:flex;align-items:center;justify-content:center;box-shadow:0 2px 4px rgba(0,0,0,.2)}

/* about */
.about-text{position:absolute;left:590px;top:874px;width:402px;font-size:10.5px;line-height:17px}
.about-text p+p{margin-top:14px}
.photo{position:absolute}
.photo-team{left:208px;top:882px;width:100px;height:178px;background:linear-gradient(160deg,#7d8d87,#a9b29a 50%,#5f6a62)}
.photo-hands{left:306px;top:864px;width:184px;height:314px;background:linear-gradient(170deg,#6b7a84,#8f8c84 40%,#a08068 70%,#6e7c5c);box-shadow:0 3px 8px rgba(0,0,0,.35);border:3px solid var(--white)}
.photo-portrait{left:490px;top:980px;width:102px;height:176px;background:linear-gradient(180deg,#d8d3cc,#b58e6c 45%,#e6e2dc)}

/* newsletter */
.newsletter{position:absolute;top:1268px;left:0;width:1200px;height:196px;background:linear-gradient(95deg,#6f6560 0%,#9d938b 30%,#8c8680 55%,#b2a79c 75%,#74665c 100%)}
.newsletter-shade{position:absolute;inset:0;background:rgba(50,45,45,.35)}
.newsletter-title{position:absolute;top:60px;left:0;width:1200px;text-align:center;color:var(--white);font-size:13px}
.newsletter-form{position:absolute;top:106px;left:374px;display:flex;height:32px}
.email-field{width:324px;background:var(--green);color:var(--white);font-family:"Poppins",sans-serif;font-size:10px;font-weight:600;display:flex;align-items:center;padding-left:14px}
.signup-btn{margin-left:4px;width:96px;background:var(--green);color:var(--white);font-family:"Poppins",sans-serif;font-size:10px;font-weight:600;display:flex;align-items:center;justify-content:center}
.newsletter-form .arrow-box{width:22px;height:22px;margin:5px 0 0 -8px}

/* teaser */
.teaser-col{position:absolute;top:1560px;width:380px;font-size:9px;line-height:16.5px;color:#7a7a7a}

/* team */
.team-band{position:absolute;top:1782px;left:0;width:1200px;height:98px;background:var(--green)}
.member{position:absolute;top:1760px;width:142px;height:142px;transform:rotate(45deg);overflow:hidden;border:4px solid var(--white);box-shadow:0 2px 6px rgba(0,0,0,.2)}
.member-card{background:var(--dark)}
.member-inner{position:absolute;left:50%;top:50%;width:200px;height:200px;margin:-100px 0 0 -100px;transform:rotate(-45deg);text-align:center;color:var(--white)}
.member-name{margin-top:74px;font-size:11px;letter-spacing:2px}
.member-role{margin-top:4px;font-size:7.5px;letter-spacing:2px;color:#bdbdbd}
.member-social{position:absolute;left:82px;top:122px;display:flex;gap:6px}
.member-social i{width:8px;height:8px;border-radius:50%;background:var(--white)}
.member-photo-a{background:linear-gradient(180deg,#e9e9e9,#8a7a6e 55%,#2f3540)}
.member-photo-b{background:linear-gradient(180deg,#f0f0f0,#6e4d3c 50%,#2d2d33)}

/* partners */
.partner{position:absolute;width:98px;height:98px;transform:rotate(45deg);border:1px solid #ededed;background:var(--white)}
.partner-mark{position:absolute;left:50%;top:50%;transform:translate(-50%,-50%) rotate(-45deg);background:#d0d0d0}
.mark-round{width:30px;height:30px;border-radius:50%}
.mark-bar{width:56px;height:14px}
.mark-square{width:28px;height:28px}

/* footer */
.footer{position:absolute;top:2372px;left:0;width:1200px;height:248px;background:var(--footer)}
.footer-col{position:absolute;top:32px;width:180px;color:#cfcfcf;font-size:9.5px;line-height:17px}
.footer-col h4{font-family:"Poppins",sans-serif;font-weight:600;font-size:11.5px;color:var(--white);margin-bottom:20px}
.footer-col u{text-decoration:underline}
.footer-social{display:flex;gap:14px;margin-top:16px}
.footer-social i{width:12px;height:12px;border-radius:50%;border:1px solid #6a6a6a}
</style>
</head>
<body>

<nav class="nav">
  <a class="active" style="left:210px">HOME</a>
  <a style="left:298px">OVER ONS</a>
  <a style="left:410px">KANDIDATEN</a>
  <div class="brand"><i></i>WERKWIJS</div>
  <a style="left:710px">VACATURES</a>
  <a style="left:806px">CONTACT</a>
  <div class="menu-icon"><span></span><span></span><span></span></div>
</nav>

<section class="hero">
  <div class="abs" style="inset:0" role="img" aria-label="Foto van twee lachende jonge vrouwen samen achter een laptop"></div>
  <div class="hero-shade"></div>
  <h1 class="hero-title heading">Zoek de perfecte baan die bij mij past</h1>
  <form class="search">
    <div class="search-field">
      <svg width="12" height="12" viewBox="0 0 12 12"><circle cx="5" cy="5" r="3.6" fill="none" stroke="#fff" stroke-width="1.6"/><line x1="7.6" y1="7.6" x2="11" y2="11" stroke="#fff" stroke-width="1.8"/></svg>
      WAT VOOR WERK WIL IK DOEN...?
    </div>
    <div class="search-select">BRANCHE
      <svg width="8" height="5" viewBox="0 0 8 5"><path d="M0 0h8L4 5z" fill="#fff"/></svg>
    </div>
    <div class="search-btn">ZOEKEN</div>
  </form>
</section>

<section class="featured">
  <h2 class="section-title heading" style="top:26px">Uitgelichte vacatures</h2>
</section>

<article class="job-card" style="left:210px">
  <h3 class="job-title">Timmerman</h3>
  <span class="job-badge">Populair</span>
  <div class="job-meta">Groningen</div>
  <p class="job-text">Lorem ipsum dolor sit amet, consectetur adipisicing elit, sed do eiusmod tempor incididunt ut labore et dolore magna aliqua. Ut enim ad minim veniam, quis nostrud exercitation ullamco laboris nisi ut aliquip ex ea commodo consequat. Duis aute</p>
  <div class="read-more"><b>LEES MEER</b><span class="arrow-box"><svg width="6" height="8" viewBox="0 0 6 8"><path d="M1 0l4 4-4 4" fill="none" stroke="#fff" stroke-width="1.5"/></svg></span></div>
</article>
<article class="job-card" style="left:408px">
  <h3 class="job-title highlight"><span>Laster weekendhulp bij avonduren</span></h3>
  <div class="job-meta">Amsterdam</div>
  <p class="job-text" style="height:110px">Lorem ipsum dolor sit amet, consectetur adipisicing elit, sed do eiusmod tempor incididunt ut labore et dolore magna aliqua. Ut enim ad minim veniam, quis nostrud exercitation ullamco laboris nisi ut aliquip ex ea commodo consequat. Duis aute</p>
  <div class="read-more"><b>LEES MEER</b><span class="arrow-box"><svg width="6" height="8" viewBox="0 0 6 8"><path d="M1 0l4 4-4 4" fill="none" stroke="#fff" stroke-width="1.5"/></svg></span></div>
</article>
<article class="job-card" style="left:608px">
  <h3 class="job-title">Junior webdesigner</h3>
  <div class="job-meta">Arnhem</div>
  <p class="job-text">Lorem ipsum dolor sit amet, consectetur adipisicing elit, sed do eiusmod tempor incididunt ut labore et dolore magna aliqua. Ut enim ad minim veniam, quis nostrud exercitation ullamco laboris nisi ut aliquip ex ea commodo consequat. Duis aute</p>
  <div class="read-more"><b>LEES MEER</b><span class="arrow-box"><svg width="6" height="8" viewBox="0 0 6 8"><path d="M1 0l4 4-4 4" fill="none" stroke="#fff" stroke-width="1.5"/></svg></span></div>
</article>
<article class="job-card" style="left:808px">
  <h3 class="job-title">PHP-programmeur</h3>
  <span class="job-badge">Nieuw</span>
  <div class="job-meta">Groningen</div>
  <p class="job-text">Lorem ipsum dolor sit amet, consectetur adipisicing elit, sed do eiusmod tempor incididunt ut labore et dolore magna aliqua. Ut enim ad minim veniam, quis nostrud exercitation ullamco laboris nisi ut aliquip ex ea commodo consequat. Duis aute</p>
  <div class="read-more"><b>LEES MEER</b><span class="arrow-box"><svg width="6" height="8" viewBox="0 0 6 8"><path d="M1 0l4 4-4 4" fill="none" stroke="#fff" stroke-width="1.5"/></svg></span></div>
</article>
<a class="all-jobs heading">Alle vacatures</a>

<h2 class="section-title heading" style="top:802px">Over Werkwijs</h2>
<div class="photo photo-team" role="img" aria-label="Foto van collega's die samen overleggen"></div>
<div class="photo photo-portrait" role="img" aria-label="Portretfoto van een medewerker in kantooromgeving"></div>
<div class="photo photo-hands" role="img" aria-label="Foto van een team dat de handen op elkaar legt"></div>
<div class="about-text">
  <p>Lorem ipsum dolor sit amet, consectetur adipisicing elit, sed do eiusmod tempor incididunt ut labore et dolore magna aliqua. Ut enim ad minim veniam, quis nostrud exercitation ullamco laboris nisi ut aliquip ex ea commodo consequat. Duis aute irure dolor in reprehenderit in voluptate velit esse cillum dolore eu fugiat nulla pariatur. Excepteur sint occaecat cupidatat non proident, sunt in culpa qui officia deserunt mollit anim id est laborum.</p>
  <p>Veritatis et quasi architecto beatae vitae dicta sunt explicabo. Nemo enim ipsam voluptatem quia voluptas sit aspernatur aut odit aut fugit, sed quia consequuntur magni dolores eos qui ratione voluptatem sequi nesciunt. Neque porro quisquam est, qui dolorem ipsum quia dolor sit amet, consectetur, adipisci velit, sed quia non numquam eius modi tempora incidunt ut labore et dolore magnam aliquam quaerat voluptatem.</p>
</div>

<section class="newsletter">
  <div class="abs" style="inset:0" role="img" aria-label="Vervaagde foto van een vrouw met een telefoon op kantoor"></div>
  <div class="newsletter-shade"></div>
  <h2 class="newsletter-title heading">Aanmelden voor de nieuwsbrief</h2>
  <form class="newsletter-form">
    <div class="email-field">JE EMAIL ADRES</div>
    <div class="signup-btn">AANMELDEN</div>
    <span class="arrow-box"><svg width="6" height="8" viewBox="0 0 6 8"><path d="M1 0l4 4-4 4" fill="none" stroke="#fff" stroke-width="1.5"/></svg></span>
  </form>
</section>

<h2 class="section-title heading" style="top:1508px;font-size:13px">Vrije teaser om zelf in te vullen</h2>
<p class="teaser-col" style="left:210px">Lorem ipsum dolor sit amet, consectetur adipisicing elit, sed do eiusmod tempor incididunt ut labore et dolore magna aliqua. Ut enim ad minim veniam, quis nostrud exercitation ullamco laboris nisi ut aliquip ex ea commodo consequat. Duis aute irure dolor in reprehenderit in voluptate velit esse cillum dolore eu fugiat nulla pariatur. Excepteur sint occaecat cupidatat non proident, sunt in</p>
<p class="teaser-col" style="left:610px">Perspiciatis unde omnis iste natus error sit voluptatem accusantium doloremque laudantium, totam rem aperiam, eaque ipsa quae ab illo inventore veritatis et quasi architecto beatae vitae dicta sunt explicabo. Nemo enim ipsam voluptatem quia voluptas sit aspernatur aut odit aut fugit, sed quia consequuntur magni dolores eos qui ratione voluptatem sequi nesciunt. Neque porro quisquam est, qui dolorem ipsum quia</p>

<h2 class="section-title heading" style="top:1708px">Wie zijn wij?</h2>
<div class="team-band"></div>
<div class="member member-card" style="left:231px">
  <div class="member-inner">
    <div class="member-name heading">Sanne Vermeer</div>
    <div class="member-role heading">Recruiter</div>
    <div class="member-social"><i></i><i></i><i></i></div>
  </div>
</div>
<div class="member member-photo-a" style="left:529px" role="img" aria-label="Portretfoto van een medewerker in pak"></div>
<div class="member member-photo-b" style="left:829px" role="img" aria-label="Portretfoto van een medewerkster in blazer"></div>

<h2 class="section-title heading" style="top:1996px;font-size:13px">Met wie werkt Werkwijs samen?</h2>
<div class="partner" style="left:411px;top:2059px"><span class="partner-mark mark-square"></span></div>
<div class="partner" style="left:551px;top:2059px"><span class="partner-mark mark-bar"></span></div>
<div class="partner" style="left:691px;top:2059px"><span class="partner-mark mark-bar"></span></div>
<div class="partner" style="left:343px;top:2127px"><span class="partner-mark mark-round"></span></div>
<div class="partner" style="left:483px;top:2127px"><span class="partner-mark mark-bar"></span></div>
<div class="partner" style="left:623px;top:2127px"><span class="partner-mark mark-bar"></span></div>
<div class="partner" style="left:763px;top:2127px"><span class="partner-mark mark-bar"></span></div>
<div class="partner" style="left:411px;top:2195px"><span class="partner-mark mark-round"></span></div>
<div class="partner" style="left:551px;top:2195px"><span class="partner-mark mark-bar"></span></div>
<div class="partner" style="left:691px;top:2195px"><span class="partner-mark mark-square"></span></div>

<footer class="footer">
  <div class="footer-col" style="left:210px">
    <h4>Over ons</h4>
    Aliquam luctus nulla augue, quis aliquet leo porta tincidunt. Donec turpis tellus, luctus eu neque lobortis, eleifend facilisis mauris. Aenean sodales sapien diam. Morbi dignissim nibh eu tempor pharetra. Nam ac nibh porttitor.
  </div>
  <div class="footer-col" style="left:410px">
    <h4>RSS</h4>
    Praesent quis Donec in accumsan <u>porta tincidunt. Donec turpis tellus, luctus eu neque</u><br><br>
    et rhoncus lectus erat pellentes que odio. In commodo
  </div>
  <div class="footer-col" style="left:608px">
    <h4>Vacatures</h4>
    Lorem ipsum dolor sit amet, consectetur adipisicing elit, sed do eiusmod tempor incididunt ut labore et dolore magna aliqua. Ut enim ad minim veniam, aliquip ex ea commodo
  </div>
  <div class="footer-col" style="left:808px">
    <h4>Contact</h4>
    Werkwijs B.V.<br>Kanaalstraat 12B<br>1054 XK Amsterdam
    <div class="footer-social"><i></i><i></i><i></i></div>
  </div>
</footer>

</body>
</html>
```